Checkout sign

Wall sign for clinic checkout.
“The Good Lord does ALL the healing..
But we DO collect the co-pay”

Add Celtic cross at top and our logo on bottom

```html
<!DOCTYPE html>
<html lang="en">
<head>
<meta charset="utf-8">
<title>Checkout Sign – Brennan Orthopedic Clinic</title>
<link href="https://fonts.googleapis.com/css2?family=Barlow+Condensed:wght@600&display=swap" rel="stylesheet">
<style>
  :root {
    --navy: #1a1a8c;
    --navy-soft: #3a3aa6;
    --white: #ffffff;
  }
  html, body {
    margin: 0;
    padding: 0;
    overflow: hidden;
    background: var(--white);
  }
  .sign {
    position: relative;
    width: 965px;
    height: 1200px;
    background: var(--white);
    overflow: hidden;
    font-family: "Barlow Condensed", "Arial Narrow", sans-serif;
  }
  .sign__panel {
    position: absolute;
    left: 75px;
    top: 275px;
    width: 815px;
    height: 664px;
    background: var(--navy);
  }
  .sign__frame {
    position: absolute;
    left: 111px;
    top: 304px;
    width: 737px;
    height: 600px;
    border: 3px solid var(--white);
    border-radius: 3px;
  }
  .sign__cross {
    position: absolute;
    left: 396px;
    top: 33px;
    width: 174px;
    height: 274px;
    background: linear-gradient(180deg, var(--navy-soft), var(--navy));
    border-radius: 6px;
  }
  .sign__line {
    position: absolute;
    left: 75px;
    width: 815px;
    text-align: center;
    color: var(--white);
    font-weight: 600;
    font-size: 93px;
    line-height: 1;
    white-space: nowrap;
  }
  .sign__line--1 { top: 366px; }
  .sign__line--2 { top: 462px; }
  .sign__line--3 { top: 646px; }
  .sign__line--4 { top: 741px; }
  .brand {
    position: absolute;
    left: 0;
    top: 988px;
    width: 965px;
    text-align: center;
    color: var(--navy);
    font-weight: 600;
  }
  .brand__mark {
    width: 114px;
    height: 114px;
    margin: 0 auto 8px;
    border: 3px solid var(--navy);
    border-radius: 50%;
    box-sizing: border-box;
  }
  .brand__name {
    font-size: 40px;
    line-height: 1;
    letter-spacing: 1px;
  }
  .brand__sub {
    font-size: 16px;
    line-height: 1.2;
    letter-spacing: 2px;
    text-transform: uppercase;
  }
</style>
</head>
<body>
  <main class="sign">
    <div class="sign__panel"></div>
    <div class="sign__frame"></div>
    <div class="sign__cross" role="img" aria-label="Celtic cross with knotwork ornament"></div>

    <p class="sign__line sign__line--1" style="margin:0">“The GOOD LORD does</p>
    <p class="sign__line sign__line--2" style="margin:0">ALL the healing..</p>
    <p class="sign__line sign__line--3" style="margin:0">But we DO collect</p>
    <p class="sign__line sign__line--4" style="margin:0">the co-pay”</p>

    <div class="brand">
      <div class="brand__mark"></div>
      <div class="brand__name">BRENNAN</div>
      <div class="brand__sub">Orthopedic Clinic</div>
    </div>
  </main>
</body>
</html>
```